Plakat-Design für Cloud-Telefonanlage
Zielgruppe
https://www.veltrada-beispiel.at/festnetz/business/virtuelle-cloud-telefonanlage
Aufgabenstellung
rollup_xxl_200x300 Grafik - siehe Datenblatt
Überschrift groß: Cloud Telefonanlage aus Tirol
Evt. dann die Features aufzählen [?] dazu hätte ich den Text u. die
Grafik im Anhang 'Cloud-Features' beigefügt.
**** Änderung am 17.06 **** : Die Features nur benennen, sprich ohne Beschreibung! Wird dann zu viel Inhalt.
Hinzufügen:
Computer Telefon Integration (CTI)
Konferenzen
Smartphone App
Sprachaufzeichnungen
Fax2Mail - Mail2Fax
Farbcode: A46CA0

```html
<!DOCTYPE html>
<html lang="de">
<head>
<meta charset="utf-8">
<title>Cloud Telefonanlage aus Tirol – Veltrada</title>
<link rel="stylesheet" href="https://fonts.googleapis.com/css2?family=Montserrat:ital,wght@0,300;0,700;0,800;1,500&family=Montserrat+Alternates:ital,wght@1,600&display=swap">
<style>
  :root {
    --brand: #a46ca0;
    --ink: #0d0d0d;
    --label: #1a1a1a;
    --page: #ffffff;
    --wave-light: #f9f7fa;
    --wave-soft: #f4ecf2;
  }
  * { margin: 0; padding: 0; box-sizing: border-box; }
  html, body {
    width: 750px; height: 1200px; overflow: hidden;
    background: var(--page);
  }
  .poster {
    position: absolute; left: 0; top: 37.5px;
    width: 750px; height: 1125px;
    background: var(--page);
    overflow: hidden;
  }
  .poster__waves { position: absolute; inset: 0; width: 750px; height: 1125px; }
  .brand-name {
    position: absolute; right: 48px; top: 40px;
    font-family: "Montserrat", sans-serif; font-weight: 800;
    font-size: 32px; letter-spacing: 0.01em; color: var(--ink);
    display: flex; align-items: center; gap: 10px;
  }
  .brand-name__dot {
    width: 12px; height: 12px; border-radius: 50%; background: var(--brand);
  }
  .headline {
    position: absolute; left: 69px; top: 118px;
    font-family: "Montserrat", sans-serif; color: var(--ink);
    line-height: 1;
  }
  .headline__light {
    display: block; font-weight: 300; font-size: 47px; letter-spacing: 0.08em;
  }
  .headline__bold {
    display: block; margin-top: 6px; font-weight: 700; font-size: 47px; letter-spacing: 0.085em;
  }
  .rule {
    position: absolute; left: 0; top: 228px; width: 366px; height: 2px; background: var(--brand);
  }
  .tagline {
    position: absolute; left: 381px; top: 219px;
    font-family: "Montserrat", sans-serif; font-style: italic; font-weight: 500;
    font-size: 17px; color: var(--brand); line-height: 20px;
  }
  .features {
    position: absolute; left: 30px; top: 310px;
    width: 648px;
    display: grid;
    grid-template-columns: 324px 324px;
    grid-auto-rows: 67px;
    row-gap: 22px;
    list-style: none;
  }
  .feature {
    display: flex; flex-direction: column; align-items: center;
  }
  .feature--wide { grid-column: 1 / span 2; }
  .feature__icon { width: 32px; height: 32px; fill: var(--brand); }
  .feature__label {
    margin-top: 17px;
    font-family: "Montserrat Alternates", sans-serif; font-style: italic; font-weight: 600;
    font-size: 12.5px; line-height: 16px; color: var(--label); white-space: nowrap;
  }
</style>
</head>
<body>
<main class="poster">
  <svg class="poster__waves" viewBox="0 0 750 1125" aria-hidden="true">
    <path fill="var(--wave-light)" d="M0 455 C80 425 200 420 300 470 C380 510 420 570 450 610 C500 670 580 720 650 700 C700 690 730 668 750 628 L750 1125 L0 1125 Z"/>
    <path fill="var(--wave-soft)" d="M0 665 C90 635 220 635 320 690 C380 722 410 765 440 800 C490 860 560 895 620 880 C680 868 720 835 750 795 L750 1125 L0 1125 Z"/>
  </svg>

  <div class="brand-name"><span>Veltrada</span><span class="brand-name__dot"></span></div>

  <h1 class="headline">
    <span class="headline__light">CLOUD</span>
    <span class="headline__bold">TELEFONANLAGE</span>
  </h1>
  <div class="rule"></div>
  <p class="tagline">AUS TIROL</p>

  <ul class="features">
    <li class="feature">
      <svg class="feature__icon" viewBox="0 0 24 24"><path d="M6.6 2.5c.6-.3 1.3-.1 1.6.5l1.7 3.5c.3.6.1 1.2-.4 1.6L8 9.2c.9 2.4 2.8 4.6 5.1 5.9l1.2-1.4c.4-.5 1.1-.6 1.6-.3l3.3 2c.6.3.8 1 .6 1.6l-.9 2.6c-.2.6-.8 1-1.4.9C10.3 19.8 4.3 13.4 3.7 6.2c0-.6.3-1.2.9-1.4z"/></svg>
      <span class="feature__label">Telefoniefunktion</span>
    </li>
    <li class="feature">
      <svg class="feature__icon" viewBox="0 0 24 24"><path d="M9 2h6v5h-2v3h8v4h1.5v6h-6v-6H18v-2H6v2h1.5v6h-6v-6H3v-4h8V7H9zm2 2v1h2V4zM4 16v2h1.5v-2zm14.5 0v2H20v-2z"/></svg>
      <span class="feature__label">Durchwahlen Verwaltung</span>
    </li>
    <li class="feature">
      <svg class="feature__icon" viewBox="0 0 24 24"><path d="M4 4h6v3H6v10h4v3H4c-1 0-2-1-2-2V6c0-1 1-2 2-2zm9 4h4V4l6 8-6 8v-4h-4c-.6 0-1-.4-1-1V9c0-.6.4-1 1-1z"/></svg>
      <span class="feature__label">Routing &amp; Weiterleitungen</span>
    </li>
    <li class="feature">
      <svg class="feature__icon" viewBox="0 0 24 24"><path d="M12 1.5a10.5 10.5 0 1 1 0 21 10.5 10.5 0 0 1 0-21zm-1.2 4.5v6.6l3.8 3 1.3-1.6-2.7-2.2V6z"/></svg>
      <span class="feature__label">Geschäftszeiten</span>
    </li>
    <li class="feature">
      <svg class="feature__icon" viewBox="0 0 24 24"><circle cx="12" cy="7" r="3.4"/><circle cx="5" cy="8.5" r="2.2"/><circle cx="19" cy="8.5" r="2.2"/><path d="M7 19v-2.5C7 13.5 9 12 12 12s5 1.5 5 4.5V19zM1 16.5C1 14 2.5 12.5 5 12.5c.8 0 1.5.2 2 .5-.8.9-1.3 2.1-1.3 3.5zM23 16.5c0-2.5-1.5-4-4-4-.8 0-1.5.2-2 .5.8.9 1.3 2.1 1.3 3.5z"/></svg>
      <span class="feature__label">Anrufgruppen</span>
    </li>
    <li class="feature">
      <svg class="feature__icon" viewBox="0 0 24 24"><rect x="3" y="4" width="18" height="2.6" rx=".5"/><rect x="3" y="10.7" width="18" height="2.6" rx=".5"/><rect x="3" y="17.4" width="18" height="2.6" rx=".5"/></svg>
      <span class="feature__label">IVR-Menü</span>
    </li>
    <li class="feature">
      <svg class="feature__icon" viewBox="0 0 24 24"><path d="M20 3h1.5v14H20l-7-4.5H9.5l1.3 6c.1.6-.3 1.2-.9 1.2H8c-.5 0-.9-.3-1-.8L5.4 12.5H4c-1.1 0-2-.9-2-2V8c0-1.1.9-2 2-2h9zm-1.5 3L13.5 8.5v2l5 2.5z"/><rect x="22" y="8" width="1.5" height="4" rx=".7"/></svg>
      <span class="feature__label">Ansagen</span>
    </li>
    <li class="feature">
      <svg class="feature__icon" viewBox="0 0 24 24"><path d="M12 1.5a5 5 0 0 1 5 5V10h1.5c.8 0 1.5.7 1.5 1.5V21c0 .8-.7 1.5-1.5 1.5h-13C4.7 22.5 4 21.8 4 21v-9.5C4 10.7 4.7 10 5.5 10H7V6.5a5 5 0 0 1 5-5zm0 2.5a2.5 2.5 0 0 0-2.5 2.5V10h5V6.5A2.5 2.5 0 0 0 12 4z"/></svg>
      <span class="feature__label">Anrufsperren &amp; Gesprächslimit</span>
    </li>
    <li class="feature">
      <svg class="feature__icon" viewBox="0 0 24 24"><path d="M6 5h12c.7 0 1.2.4 1.5 1l3 6.5V18c0 1-.8 2-2 2H3.5c-1.1 0-2-1-2-2v-5.5l3-6.5C4.8 5.4 5.3 5 6 5zm.6 2.5-2.2 5H9l1 2h4l1-2h4.6l-2.2-5z"/></svg>
      <span class="feature__label">Virtuelle Sprachbox (Voice2Mail)</span>
    </li>
    <li class="feature">
      <svg class="feature__icon" viewBox="0 0 24 24"><path d="M5 1.5h13c.8 0 1.5.7 1.5 1.5v18c0 .8-.7 1.5-1.5 1.5H5c-.8 0-1.5-.7-1.5-1.5V3c0-.8.7-1.5 1.5-1.5zm6.5 5.5a2.3 2.3 0 1 0 0 4.6 2.3 2.3 0 0 0 0-4.6zM7.5 16.5h8c0-2.2-1.8-3.6-4-3.6s-4 1.4-4 3.6z"/><rect x="20" y="4.5" width="2" height="3" rx=".6"/><rect x="20" y="10.5" width="2" height="3" rx=".6"/><rect x="20" y="16.5" width="2" height="3" rx=".6"/></svg>
      <span class="feature__label">Globales Telefonbuch</span>
    </li>
    <li class="feature">
      <svg class="feature__icon" viewBox="0 0 24 24"><path d="M4 1.5c.5-.2 1.1 0 1.3.5l1.5 3c.2.5.1 1-.3 1.4l-1 .9c.4 1.2 1 2.3 1.8 3.3l-2.3 2.3C3.2 10.5 2 7.5 2 4.5c0-.5.3-1 .8-1.2zM14.5 17.7l1.1-1.2c.4-.4 1-.5 1.4-.2l2.8 1.7c.5.3.7.9.5 1.4l-.8 2.2c-.2.5-.7.8-1.2.8-3 .1-6-1-8.5-2.8l2.3-2.3c.8.5 1.6.9 2.4 1.2z"/><rect x="10.5" y="0" width="2" height="26" rx="1" transform="rotate(52 12 12)"/></svg>
      <span class="feature__label">Verpasste Anrufe &amp; Logs</span>
    </li>
    <li class="feature">
      <svg class="feature__icon" viewBox="0 0 24 24"><path d="M2 2.5h2.2v17h18.3v2.2H2z"/><rect x="7" y="12" width="2.4" height="5" rx=".4"/><rect x="11" y="9" width="2.4" height="8" rx=".4"/><rect x="15" y="11" width="2.4" height="6" rx=".4"/><rect x="19" y="5.5" width="2.4" height="11.5" rx=".4"/></svg>
      <span class="feature__label">Anrufstatistiken</span>
    </li>
    <li class="feature">
      <svg class="feature__icon" viewBox="0 0 24 24"><path d="M2.5 3h15c.8 0 1.5.7 1.5 1.5V8h-2V5H3v10h9v2H9.5v2H12v2H5v-2h2.5v-2h-5c-.8 0-1.5-.7-1.5-1.5v-11C1 3.7 1.7 3 2.5 3z"/><rect x="14" y="9.5" width="8.5" height="13" rx="1.2"/></svg>
      <span class="feature__label">Computer Telefon Integration (CTI)</span>
    </li>
    <li class="feature">
      <svg class="feature__icon" viewBox="0 0 24 24"><path d="M3 2.5h11c.8 0 1.5.7 1.5 1.5v7c0 .8-.7 1.5-1.5 1.5H8l-4 3.5v-3.5H3c-.8 0-1.5-.7-1.5-1.5V4c0-.8.7-1.5 1.5-1.5z"/><path d="M17.5 7.5H21c.8 0 1.5.7 1.5 1.5v7c0 .8-.7 1.5-1.5 1.5h-1V21l-4-3.5h-5c-.8 0-1.5-.7-1.5-1.5v-2h5c1.7 0 3-1.3 3-3z"/></svg>
      <span class="feature__label">Konferenzen</span>
    </li>
    <li class="feature">
      <svg class="feature__icon" viewBox="0 0 24 24"><path d="M7.5 1h9c1.1 0 2 .9 2 2v18c0 1.1-.9 2-2 2h-9c-1.1 0-2-.9-2-2V3c0-1.1.9-2 2-2zm.5 3v14h8V4zm4 15.5a1.2 1.2 0 1 0 0 2.4 1.2 1.2 0 0 0 0-2.4z"/></svg>
      <span class="feature__label">Smartphone App</span>
    </li>
    <li class="feature">
      <svg class="feature__icon" viewBox="0 0 24 24"><path d="M12 1.5a3.5 3.5 0 0 1 3.5 3.5v6a3.5 3.5 0 0 1-7 0V5A3.5 3.5 0 0 1 12 1.5z"/><path d="M5 10h2a5 5 0 0 0 10 0h2a7 7 0 0 1-6 6.9V20h3v2.5H8V20h3v-3.1A7 7 0 0 1 5 10z"/></svg>
      <span class="feature__label">Sprachaufzeichnungen</span>
    </li>
    <li class="feature feature--wide">
      <svg class="feature__icon" viewBox="0 0 24 24"><path d="M3 4.5h18c.8 0 1.5.7 1.5 1.5v.6L12 13.2 1.5 6.6V6c0-.8.7-1.5 1.5-1.5zM1.5 9l10.5 6.6L22.5 9v9c0 .8-.7 1.5-1.5 1.5H3c-.8 0-1.5-.7-1.5-1.5z"/></svg>
      <span class="feature__label">Fax2Mail – Mail2Fax</span>
    </li>
  </ul>
</main>
</body>
</html>
```